Harbor Crest Motors

I’m looking for artwork that can go on the back of my vehicles that I sell. It’s going to be a magnet on the back of the vehicle. On the magnet it needs to state - I am for sale!
Please visit - harborcrestmotors.com

And in all caps - WE BEAT ANY PRICE!

Logo attached

Target Market(s)

Car sales

Industry/Entity Type

Car sales

```html
<!DOCTYPE html>
<html lang="en">
<head>
<meta charset="utf-8">
<title>Harbor Crest Motors – Vehicle Magnet</title>
<link rel="stylesheet" href="https://fonts.googleapis.com/css2?family=Anton&display=swap">
<style>
  :root {
    --page-bg: #ffffff;
    --magnet-black: #000000;
    --band-yellow: #fff200;
    --headline-white: #ffffff;
    --band-ink: #000000;
  }
  html, body {
    margin: 0;
    padding: 0;
    width: 1200px;
    height: 1000px;
    overflow: hidden;
    background: var(--page-bg);
  }
  .canvas {
    display: block;
    width: 1200px;
    height: 1000px;
  }
  .magnet-body { fill: var(--magnet-black); }
  .info-band { fill: var(--band-yellow); }
  .sale-tag,
  .dealer-name,
  .dealer-site,
  .headline {
    font-family: "Anton", "Bebas Neue", sans-serif;
  }
  .sale-tag,
  .dealer-name,
  .headline { text-transform: uppercase; }
  .sale-tag { fill: var(--band-ink); font-size: 45px; }
  .dealer-name { fill: var(--band-ink); font-size: 32px; }
  .dealer-site { fill: var(--band-ink); font-size: 13px; letter-spacing: 0.5px; }
  .headline { fill: var(--headline-white); font-size: 132px; }
</style>
</head>
<body>
<svg class="canvas" viewBox="0 0 1200 1000" xmlns="http://www.w3.org/2000/svg" role="img" aria-label="Harbor Crest Motors magnet: I am for sales, we beat any prices, harborcrestmotors.com">
  <rect class="magnet-body" x="172" y="362" width="821" height="253"/>
  <rect class="info-band" x="193" y="383" width="774" height="64"/>

  <g transform="translate(203 436) skewX(-14)">
    <text class="sale-tag" x="0" y="0" textLength="266" lengthAdjust="spacingAndGlyphs">I am for sales</text>
  </g>

  <text class="dealer-name" x="722" y="425" textLength="236" lengthAdjust="spacingAndGlyphs">Harbor Crest Motors</text>
  <text class="dealer-site" x="818" y="442" textLength="140" lengthAdjust="spacingAndGlyphs">harborcrestmotors.com</text>

  <g transform="translate(195 584) skewX(-10)">
    <text class="headline" x="0" y="0" textLength="752" lengthAdjust="spacingAndGlyphs">We beat any prices</text>
  </g>
</svg>
</body>
</html>
```